The Perfect Business Card for PineHarbor

I am looking for a business card which beautifully incorporates my logo, reflects my business and looks special, elegant and clean.

```html
<!DOCTYPE html>
<html lang="en">
<head>
<meta charset="utf-8">
<title>PineHarbor Business Card</title>
<link rel="stylesheet" href="https://fonts.googleapis.com/css2?family=Open+Sans:wght@400;600;800&display=swap">
<style>
  :root {
    --bg: #e9e8e4;
    --green-dark: #4b6a1f;
    --green: #6a8a34;
    --green-light: #7a9b3c;
    --ink: #3c3c3c;
    --white: #ffffff;
  }
  * { box-sizing: border-box; margin: 0; padding: 0; }
  html, body { width: 1200px; height: 913px; overflow: hidden; }
  body {
    background: var(--bg);
    font-family: "Open Sans", sans-serif;
    display: flex;
    align-items: center;
    justify-content: center;
    gap: 60px;
  }
  .card {
    width: 525px;
    height: 300px;
    border-radius: 18px;
    position: relative;
    overflow: hidden;
    box-shadow: 0 6px 18px rgba(0,0,0,0.18);
  }
  .card-back {
    background: linear-gradient(135deg, var(--green-light), var(--green-dark));
  }
  .card-back .pattern {
    position: absolute; inset: 0;
    background: linear-gradient(135deg, #76963a, #55762a);
    opacity: 0.6;
  }
  .card-back .brand {
    position: absolute;
    left: 50%; top: 50%;
    transform: translate(-50%, -50%);
    display: flex; align-items: center; gap: 12px;
    color: var(--white);
  }
  .brand-mark {
    width: 38px; height: 38px;
    border-radius: 50%;
    border: 2px solid currentColor;
  }
  .brand-name {
    font-weight: 400;
    font-size: 32px;
    letter-spacing: 1px;
  }
  .card-front { background: var(--white); }
  .card-front .edge {
    position: absolute; left: 0; right: 0; bottom: 0;
    height: 8px; background: var(--green);
  }
  .card-front .brand {
    position: absolute;
    left: 34px; top: 50%;
    transform: translateY(-50%);
    display: flex; align-items: center; gap: 10px;
    color: var(--green);
  }
  .card-front .brand-name { font-size: 28px; }
  .divider {
    position: absolute;
    left: 282px; top: 62px;
    width: 1px; height: 176px;
    background: var(--green-dark);
  }
  .contact {
    position: absolute;
    left: 300px; top: 58px;
    color: var(--ink);
    font-size: 13.5px;
    line-height: 1.45;
  }
  .contact .name {
    font-weight: 800;
    font-size: 19px;
    color: var(--green-dark);
    text-transform: uppercase;
    line-height: 1.1;
  }
  .contact .role {
    color: var(--green-light);
    font-size: 14px;
    margin-bottom: 10px;
  }
  .contact .address { margin-bottom: 10px; }
  .contact .line { display: flex; align-items: center; gap: 7px; }
  .contact svg { width: 12px; height: 12px; fill: var(--green); flex: none; }
</style>
</head>
<body>
  <section class="card card-back">
    <div class="pattern" role="img" aria-label="Embossed repeating brand pattern in green tones"></div>
    <div class="brand">
      <span class="brand-mark"></span>
      <span class="brand-name">PineHarbor</span>
    </div>
  </section>

  <section class="card card-front">
    <div class="brand">
      <span class="brand-mark"></span>
      <span class="brand-name">PineHarbor</span>
    </div>
    <div class="divider"></div>
    <div class="contact">
      <p class="name">Dana Whitlow</p>
      <p class="role">President</p>
      <p class="address">1780 Cove Landing Dr<br>Seabright CA 90417</p>
      <p class="line">
        <svg viewBox="0 0 24 24"><path d="M6.6 10.8a15 15 0 0 0 6.6 6.6l2.2-2.2c.3-.3.7-.4 1-.2 1.1.4 2.3.6 3.6.6.6 0 1 .4 1 1V20c0 .6-.4 1-1 1A17 17 0 0 1 3 4c0-.6.4-1 1-1h3.5c.6 0 1 .4 1 1 0 1.3.2 2.5.6 3.6.1.3 0 .7-.2 1z"/></svg>
        555-014-2276
      </p>
      <p class="line">
        <svg viewBox="0 0 24 24"><path d="M2 5h20v14H2z M2 5l10 8 10-8" /></svg>
        dana@pineharbor.com
      </p>
      <p class="line">
        <svg viewBox="0 0 24 24"><circle cx="12" cy="12" r="10"/></svg>
        www.pineharbor.com
      </p>
    </div>
    <div class="edge"></div>
  </section>
</body>
</html>
```